Satchel & Compass needs new business card design

I need a new business card design. I'm looking for out-of-the-box design which represents the freedom of being a location independent entrepreneur.
I offer coaching, retreats and trips.
I would like to see designs with and without the photo.
Colors I use are black (#000000), green (#25A796) and brown (#D7C38C)
Website satchelandcompass.com

Target Market(s)

location independent entrepreneurs, digital nomads, people looking to swap the 9 to 5 for a lifestyle business

Industry/Entity Type

Business

Contact Information for Business Card

Petra Varga
Your Lifestyle Business Coach, Retreat & Trip Leader
http://satchelandcompass.com
hello@satchelandcompass.com
Live a life you don't need a holiday from

Font styles to use
Serif
Sans Serif

Requirements
Must have
• One side should contain only the logo. I would also consider having the "Live a life you don't need a holiday from" on that side too (depending on how it looks)
• Please show both sides on the designs.

```html
<!DOCTYPE html>
<html lang="en">
<head>
<meta charset="utf-8">
<title>Satchel &amp; Compass — Business Card</title>
<link rel="stylesheet" href="https://fonts.googleapis.com/css2?family=Open+Sans:wght@400;600;700&display=swap">
<style>
  :root {
    --stage: #3b3532;
    --card: #0c0c0c;
    --ink: #f2f2f2;
    --ink-soft: #d9d9d9;
    --green: #25a796;
  }
  * { margin: 0; padding: 0; box-sizing: border-box; }
  html, body { width: 1200px; height: 900px; overflow: hidden; }
  body {
    background: var(--stage);
    font-family: "Open Sans", Arial, sans-serif;
    display: flex;
    align-items: center;
    justify-content: center;
    gap: 40px;
  }
  .card {
    position: relative;
    width: 520px;
    height: 300px;
    background: var(--card);
    border-radius: 3px;
    box-shadow: 0 10px 30px rgba(0,0,0,.35);
    color: var(--ink);
  }
  .brand-name {
    font-weight: 700;
    color: var(--ink);
    text-transform: uppercase;
    letter-spacing: 1px;
    white-space: nowrap;
  }
  /* contact side */
  .card-back .brand-name {
    position: absolute;
    left: 34px;
    top: 128px;
    font-size: 17px;
  }
  .divider {
    position: absolute;
    left: 250px;
    top: 58px;
    width: 1px;
    height: 118px;
    background: var(--green);
    opacity: .6;
  }
  .details {
    position: absolute;
    left: 266px;
    top: 56px;
    font-size: 12px;
    line-height: 1.45;
    color: var(--ink-soft);
  }
  .person { font-size: 14px; font-weight: 700; color: var(--ink); margin-bottom: 2px; }
  .person .first { color: var(--green); }
  .contacts { margin-top: 26px; list-style: none; }
  .contacts li { display: flex; align-items: center; gap: 8px; }
  .contacts svg { width: 9px; height: 9px; flex: none; }
  .tagline {
    position: absolute;
    left: 0; right: 0;
    bottom: 34px;
    text-align: center;
    font-size: 13px;
    letter-spacing: .3px;
    text-transform: uppercase;
    color: var(--ink);
  }
  /* logo side */
  .card-front { display: flex; align-items: center; justify-content: center; }
  .card-front .brand-name { font-size: 30px; }
</style>
</head>
<body>
  <section class="card card-back" aria-label="Contact side">
    <div class="brand-name">Satchel &amp; Compass</div>
    <div class="divider"></div>
    <div class="details">
      <p class="person"><span class="first">Petra</span> Varga</p>
      <p>Your Lifestyle Business Coach</p>
      <p>Retreat &amp; Trip Leader</p>
      <ul class="contacts">
        <li>
          <svg viewBox="0 0 10 10" aria-hidden="true"><rect x="0.5" y="1.5" width="9" height="7" fill="var(--green)"/><path d="M0.5 1.8 L5 5.5 L9.5 1.8" stroke="#0c0c0c" fill="none" stroke-width="1"/></svg>
          hello@satchelandcompass.com
        </li>
        <li>
          <svg viewBox="0 0 10 10" aria-hidden="true"><circle cx="5" cy="5" r="4.5" fill="var(--green)"/><path d="M0.5 5 H9.5 M5 0.5 C2.5 3 2.5 7 5 9.5 M5 0.5 C7.5 3 7.5 7 5 9.5" stroke="#0c0c0c" fill="none" stroke-width=".8"/></svg>
          www.satchelandcompass.com
        </li>
      </ul>
    </div>
    <p class="tagline">Live a life you don't need a holiday from</p>
  </section>

  <section class="card card-front" aria-label="Logo side">
    <div class="brand-name">Satchel &amp; Compass</div>
  </section>
</body>
</html>
```